Bright Tails Botanicals: Extracts for Pets

We need a brochure to help market the products. Bright Tails Botanicals makes Chinese Herbal Extracts for cats and dogs. We have three products to launch with. An allergy, calming, and pain formula. They are based on traditional Chinese Medicine Formulas that have been used for hundreds of years on humans and animals. I would like the logo (attached) and have one or two cat/dogs pictures. They can be any of the pics from my website. Each product should have a descrition of what it treats (can pull from website). The brochure can highlight its convient, effective, and a safe alternative. It has to include:

This statement has not been evaluated by the FDA.
This product is not intended to diagnose, treat, cure,
or prevent any disease. Bright Tails is not liable for any adverse effects.

I included a sample with some of the important info for the products - the desing does not have to be similar, just an example of the copy

*I would like the format to be in Illustrator, vector, so that I can change sizes if I need to without loosing any detail.

Target Market(s)

Pet Owners

Industry/Entity Type

Pet Care

Font styles to use
Other font styles liked:
• Universal (as logo)

Requirements
Must have
• Logo, Description of each products.
Nice to have
• Dog or cat picture

```html
<!DOCTYPE html>
<html lang="en">
<head>
<meta charset="utf-8">
<title>Bright Tails Botanicals — Complete Pet Care</title>
<link rel="stylesheet" href="https://fonts.googleapis.com/css2?family=Lato:wght@300;400;700&display=swap">
<style>
  :root {
    --paper: #ffffff;
    --leaf-dark: #4f9a3c;
    --leaf-lime: #b5d334;
    --ink: #4a4a4a;
    --ink-soft: #7a7a7a;
    --rule: #e3ecd0;
    --photo-light: #f3eee8;
    --photo-warm: #d9c2a3;
    --photo-dark: #5a4a3c;
  }
  * { box-sizing: border-box; margin: 0; padding: 0; }
  html, body {
    width: 992px; height: 1200px; overflow: hidden;
    background: var(--paper);
    font-family: "Lato", sans-serif;
  }
  .flyer {
    position: relative;
    width: 992px; height: 1200px;
    background: var(--paper);
  }

  /* Brand */
  .brand {
    position: absolute; left: 110px; top: 56px;
    display: flex; align-items: center; gap: 18px;
  }
  .brand-dot {
    width: 52px; height: 52px; border-radius: 50%;
    background: var(--leaf-lime);
  }
  .brand-name {
    font-weight: 400; font-size: 30px; line-height: 1.1;
    color: var(--leaf-dark); text-transform: uppercase; letter-spacing: 2px;
  }

  /* Headline */
  .headline {
    position: absolute; left: 106px; top: 150px;
    font-weight: 400; text-transform: uppercase;
    line-height: 1; letter-spacing: 2px;
  }
  .headline-top { display: block; font-size: 88px; color: var(--leaf-dark); }
  .headline-bottom { display: block; font-size: 88px; color: var(--leaf-lime); margin-top: 6px; }

  /* Photo */
  .pets-photo {
    position: absolute; left: 230px; top: 365px;
    width: 762px; height: 250px;
    background: linear-gradient(100deg, var(--photo-light) 0%, var(--photo-warm) 30%, var(--photo-dark) 55%, #b9a48c 78%, var(--photo-light) 100%);
  }

  /* Products */
  .products {
    position: absolute; left: 110px; top: 645px;
    width: 772px;
  }
  .products-intro {
    font-size: 20px; font-weight: 400; color: var(--leaf-dark);
    margin-bottom: 20px;
  }
  .products-intro strong { font-weight: 700; }
  .product-list {
    list-style: none;
    display: grid; grid-template-columns: repeat(3, 1fr); column-gap: 32px;
  }
  .product {
    border-top: 4px solid var(--leaf-lime);
    padding-top: 12px;
  }
  .product-name {
    font-size: 21px; font-weight: 700; color: var(--leaf-dark);
    text-transform: uppercase; letter-spacing: 1px;
    margin-bottom: 8px;
  }
  .product-text {
    font-size: 15px; font-weight: 400; line-height: 1.5; color: var(--ink);
  }

  /* Disclaimer */
  .disclaimer {
    position: absolute; left: 110px; top: 930px;
    width: 772px;
    font-size: 12.5px; font-weight: 400; line-height: 1.45; color: var(--ink-soft);
  }

  /* Contact */
  .contact-band {
    position: absolute; left: 0; top: 1010px;
    width: 992px; height: 32px;
    background: var(--leaf-lime);
  }
  .contact {
    position: absolute; left: 110px; top: 1064px;
    color: var(--leaf-lime);
  }
  .contact-title {
    font-size: 28px; font-weight: 400; text-transform: uppercase; letter-spacing: 1px;
    margin-bottom: 14px;
  }
  .contact-list {
    list-style: none; display: grid;
    grid-template-columns: auto auto; column-gap: 60px; row-gap: 10px;
    font-size: 21px; font-weight: 300;
  }
  .contact-item { display: flex; align-items: center; gap: 10px; }
  .contact-icon { width: 20px; height: 20px; flex: none; }
</style>
</head>
<body>
  <main class="flyer">
    <header class="brand">
      <span class="brand-dot" aria-hidden="true"></span>
      <span class="brand-name">Bright Tails<br>Botanicals</span>
    </header>

    <h1 class="headline">
      <span class="headline-top">Complete</span>
      <span class="headline-bottom">Pet Care</span>
    </h1>

    <div class="pets-photo" role="img" aria-label="Photo of puppies and kittens sitting in a row on a white background"></div>

    <section class="products">
      <p class="products-intro">Chinese herbal extracts for cats &amp; dogs — <strong>convenient, effective and a safe alternative.</strong></p>
      <ul class="product-list">
        <li class="product">
          <h2 class="product-name">Allergy Formula</h2>
          <p class="product-text">Soothes itchy skin, sneezing and watery eyes caused by seasonal and food allergies. Based on a classic formula used for centuries to calm heat and irritation.</p>
        </li>
        <li class="product">
          <h2 class="product-name">Calming Formula</h2>
          <p class="product-text">Eases anxiety, restlessness and stress from storms, travel, vet visits or time alone. A gentle traditional blend that settles the spirit without sedation.</p>
        </li>
        <li class="product">
          <h2 class="product-name">Pain Formula</h2>
          <p class="product-text">Supports comfort for stiff joints, muscle soreness and everyday aches in active and senior pets. Rooted in a time-tested formula that moves circulation.</p>
        </li>
      </ul>
    </section>

    <p class="disclaimer">This statement has not been evaluated by the FDA. This product is not intended to diagnose, treat, cure, or prevent any disease. Bright Tails is not liable for any adverse effects.</p>

    <div class="contact-band" aria-hidden="true"></div>

    <section class="contact">
      <h2 class="contact-title">Contact us:</h2>
      <ul class="contact-list">
        <li class="contact-item">
          <svg class="contact-icon" viewBox="0 0 20 20" aria-hidden="true">
            <rect width="20" height="20" rx="3" fill="var(--leaf-lime)"/>
            <path d="M6 4.5l2 .3.8 2.6-1.3 1a7 7 0 0 0 3.9 3.9l1-1.3 2.6.8.3 2c-.2.8-.9 1.2-1.7 1.2A10 10 0 0 1 4.8 6.2c0-.8.4-1.5 1.2-1.7z" fill="#fff"/>
          </svg>
          (800) 555-0142
        </li>
        <li class="contact-item">
          <svg class="contact-icon" viewBox="0 0 20 20" aria-hidden="true">
            <rect width="20" height="20" rx="3" fill="var(--leaf-lime)"/>
            <rect x="4" y="6" width="12" height="8" fill="none" stroke="#fff" stroke-width="1.5"/>
            <path d="M4 6l6 5 6-5" fill="none" stroke="#fff" stroke-width="1.5"/>
          </svg>
          hello@brighttailsmail.com
        </li>
        <li class="contact-item">www.brighttailsbotanicals.com</li>
      </ul>
    </section>
  </main>
</body>
</html>
```